Letterhead and compliment slip

We are a UK-based market research agency. We are looking for a new letterhead design to incorporate our logo, address details and company information. We are looking for a simple design. It should be modern. It needs to have a qualify feel. As we are UK based it needs to be designed for A4 paper size (letterhead).
I'm really looking for something simple in design terms!
Both letterhead and compliment slip need to include:
Our logo
Company address
Telephone number
Email address
Website address
Company registration number
VAT registration number
Grey and green would be a good colour scheme to fit with our logo

```html
<!DOCTYPE html>
<html lang="en">
<head>
<meta charset="utf-8">
<title>Fieldnote Research – Letterhead</title>
<link href="https://fonts.googleapis.com/css2?family=Open+Sans:wght@400;600;700&display=swap" rel="stylesheet">
<style>
  :root {
    --green: #8cc63f;
    --grey-dark: #3a3a3a;
    --grey-text: #4a4a4a;
    --grey-band: #9a9a9a;
    --backdrop: #ececec;
    --paper: #ffffff;
  }
  * { box-sizing: border-box; margin: 0; padding: 0; }
  html, body { width: 1200px; height: 784px; overflow: hidden; }
  body {
    background: var(--backdrop);
    font-family: "Open Sans", Arial, sans-serif;
    color: var(--grey-text);
    position: relative;
  }
  .letterhead {
    position: absolute;
    left: 338px; top: 22px;
    width: 523px; height: 740px;
    background: var(--paper);
    box-shadow: 0 2px 10px rgba(0,0,0,0.12);
    padding: 0 52px;
  }
  .brand {
    display: flex; align-items: center; justify-content: center; gap: 7px;
    padding-top: 42px;
  }
  .brand-dot {
    width: 14px; height: 14px; border-radius: 50%;
    background: var(--green);
  }
  .brand-name {
    font-size: 22px; font-weight: 700; color: var(--green);
    letter-spacing: -0.3px;
  }
  .salutation {
    margin-top: 62px;
    font-size: 10.5px; font-weight: 700; color: var(--grey-dark);
  }
  .letter-body p {
    margin-top: 14px;
    font-size: 9px; line-height: 1.45;
  }
  .letter-body p:first-child { margin-top: 6px; }
  .signature {
    margin-top: 22px;
    width: 110px; height: 46px;
    background: linear-gradient(90deg, #f1f1f1, #e4e4e4);
    border-radius: 3px;
  }
  .footer-box {
    position: absolute;
    left: 72px; right: 52px; bottom: 42px;
    border: 1px dashed var(--green);
    padding: 9px 10px;
    text-align: center;
    font-size: 7.5px; line-height: 1.7;
    color: var(--grey-dark);
  }
  .contact-line { display: flex; justify-content: center; gap: 10px; }
  .contact-item { display: inline-flex; align-items: center; gap: 4px; }
  .contact-item::before {
    content: ""; width: 6px; height: 6px; background: var(--green);
  }
  .company-line, .address-line { font-size: 6.8px; }
  .base-band {
    position: absolute; left: 0; right: 0; bottom: 0; height: 8px;
    background: linear-gradient(90deg, var(--green) 0 62%, var(--grey-band) 62% 100%);
  }
</style>
</head>
<body>
  <main class="letterhead">
    <header class="brand">
      <span class="brand-dot"></span>
      <span class="brand-name">Fieldnote</span>
    </header>

    <p class="salutation">Dear Mr. Ellis,</p>

    <section class="letter-body">
      <p>Lorem Ipsum is simply dummy text of the printing and typesetting industry. Lorem Ipsum has been the industry's standard dummy text ever since the 1500s, when an unknown printer took a galley of type and scrambled it to make a type specimen book. It has survived not only five centuries, but also the leap into electronic typesetting, remaining essentially unchanged.</p>
      <p>The standard chunk of Lorem Ipsum used since the 1500s is reproduced below for those interested. Sections 1.10.32 and 1.10.33 from "de Finibus Bonorum et Malorum" by Cicero are also reproduced in their exact original form, accompanied by English versions from the 1914 translation by H. Rackham</p>
      <p>Lorem Ipsum is simply dummy text of the printing and typesetting industry. Lorem Ipsum has been the industry's standard dummy text ever since the 1500s, when an unknown printer took a galley of type and scrambled it to make a type specimen book. It has survived not only five centuries, but also the leap into electronic typesetting, remaining essentially unchanged. It was popularised in the</p>
      <p>The standard chunk of Lorem Ipsum used since the 1500s is reproduced below for those interested. Sections 1.10.32 and 1.10.33 from "de Finibus Bonorum et Malorum" by Cicero are also reproduced in their exact original form, accompanied by English versions from the 1914 translation by H. Rackham</p>
      <p>The standard chunk of Lorem Ipsum used since the 1500s is reproduced below for those interested. Sections 1.10.32 and 1.10.33 from "de Finibus Bonorum et Malorum" by Cicero are also reproduced in their exact original form, accompanied by English versions from the 1914 translation by H. Rackham</p>
    </section>

    <div class="signature" role="img" aria-label="Handwritten signature of the sender"></div>

    <footer class="footer-box">
      <div class="contact-line">
        <span class="contact-item">+44 (0)1632 960418</span>
        <span class="contact-item">hello@fieldnoteresearch.co.uk</span>
        <span class="contact-item">www.fieldnoteresearch.co.uk</span>
      </div>
      <div class="company-line">Company registration number: 08412376 &nbsp;·&nbsp; VAT registration number: 214583761</div>
      <div class="address-line">12 Linden Yard, Mill Lane, Larkfield, Hertfordshire, AL9 4QT</div>
    </footer>

    <div class="base-band"></div>
  </main>
</body>
</html>
```